Business letterhead and powerpoint template

Hi, I have recently started using a new logo (found through PixelGrove) and would now like to use that logo for letterheads and powerpoint.

Attached is the logo and one version of a brochure I have recently used.

Industry/Entity Type

Business

```html
<!DOCTYPE html>
<html lang="en">
<head>
<meta charset="utf-8">
<title>Halden Capital — Letterhead</title>
<link rel="stylesheet" href="https://fonts.googleapis.com/css2?family=Open+Sans:wght@400&display=swap">
<style>
  :root {
    --paper: #ffffff;
    --ink: #231f20;
    --accent: #f15a24;
    --footer-dark: #1c1616;
    --footer-text: #ffffff;
  }
  * { margin: 0; padding: 0; box-sizing: border-box; }
  html, body {
    width: 933px;
    height: 1200px;
    overflow: hidden;
    background: var(--paper);
  }
  .letterhead {
    position: relative;
    width: 933px;
    height: 1200px;
    background: var(--paper);
    font-family: "Open Sans", Arial, sans-serif;
  }
  .brand {
    position: absolute;
    top: 96px;
    left: 0;
    width: 100%;
    display: flex;
    justify-content: center;
    align-items: center;
    gap: 16px;
  }
  .brand-dot {
    width: 22px;
    height: 22px;
    border-radius: 50%;
    background: var(--accent);
  }
  .brand-name {
    font-size: 44px;
    font-weight: 400;
    letter-spacing: 3px;
    color: var(--ink);
    line-height: 1;
  }
  .address-band {
    position: absolute;
    left: 0;
    top: 1118px;
    width: 100%;
    height: 35px;
    background: var(--accent);
    color: var(--footer-text);
    font-size: 14px;
    display: flex;
    justify-content: center;
    align-items: center;
  }
  .contact-band {
    position: absolute;
    left: 0;
    top: 1153px;
    width: 100%;
    height: 47px;
    background: var(--footer-dark);
    color: var(--footer-text);
    font-size: 14px;
    display: flex;
    justify-content: center;
    align-items: center;
    gap: 16px;
  }
  .contact-item {
    display: flex;
    align-items: center;
    gap: 5px;
  }
  .contact-item svg { width: 11px; height: 11px; fill: none; stroke: var(--footer-text); stroke-width: 1.4; }
</style>
</head>
<body>
  <main class="letterhead">
    <header class="brand">
      <span class="brand-dot"></span>
      <span class="brand-name">HALDEN CAPITAL</span>
    </header>

    <footer>
      <div class="address-band">Level 8 Suite 14 42 Harbour Lane Northbridge 2100 NSW Australia</div>
      <div class="contact-band">
        <span class="contact-item">
          <svg viewBox="0 0 12 12" aria-hidden="true"><path d="M3 1 L5 3.5 L4 5 Q5.5 7.5 7 8 L8.5 7 L11 9 L9.5 11 Q4 10 1 2.5 Z"/></svg>
          +61 (0)2 5550 1842
        </span>
        <span class="contact-item">
          <svg viewBox="0 0 12 12" aria-hidden="true"><rect x="1.5" y="5" width="9" height="5"/><rect x="3.5" y="1.5" width="5" height="3.5"/></svg>
          61 (0)2 5550 1100
        </span>
        <span class="contact-item">
          <svg viewBox="0 0 12 12" aria-hidden="true"><circle cx="6" cy="6" r="4.8"/><ellipse cx="6" cy="6" rx="2" ry="4.8"/><path d="M1.2 6 H10.8"/></svg>
          www.haldencapital.com.au
        </span>
      </div>
    </footer>
  </main>
</body>
</html>
```